Corvell Tarn manufacturing Project

We are looking at getting a brand new design for a new company that deals in selling stainless tubing and other stainless still products such as handrails, Spigots, Balustrade Fittings
Glass, Glass fittings and Aluminium Channels

We require a very clean website that deals with the following colours:

Blue to light blues
Blacks
Greys to light Greys
Whites

We are open for other ideas BUT we *DO NOT* want any pinks, greens or bright colours except for backgrounds colours we have chosen above. (It can be solid, gradient or a subtle pattern)

YOU MUST KEEP THE LOGO AS IS. PLEASE DO NOT ALTER THE LOGO IN *ANY WAY* and the logo MUST be the same colours and fonts.

Logo is attached.

The site must contain these aspects:
jQuery Slider (Image slide show)
Top drop down Menus
Be no more than 900px wide
Text is to be to the k9R standards. (no special fonts)

We will chop up the design into html format. You just need to provide the PSD file.

The clients opposition is:
www.polbrenwick.com

It Company

• Alter the logo in anyway

```html
<!DOCTYPE html>
<html lang="en">
<head>
<meta charset="utf-8">
<title>Harlow Birch Metal</title>
<link rel="stylesheet" href="https://fonts.googleapis.com/css2?family=Libre+Baskerville:wght@400;700&family=Open+Sans:wght@400;600&family=Raleway:wght@400;500&display=swap">
<style>
:root{
  --blue-dark:#2d5280;
  --blue:#3d6797;
  --blue-light:#6a8fbb;
  --sky:#8fb2dc;
  --ink:#1a1a1a;
  --text:#555;
  --grey-line:#dcdcdc;
  --footer:#3b3b3b;
  --white:#fff;
}
*{box-sizing:border-box;margin:0;padding:0}
html,body{width:1066px;height:1200px;overflow:hidden}
body{position:relative;font-family:Arial,Helvetica,sans-serif;color:var(--text);
  background:linear-gradient(180deg,var(--sky) 0%,#cfdff0 30%,#f4f7fb 60%,#fff 90%)}
.abs{position:absolute}
h2{font-weight:400}
.page{position:absolute;left:98px;top:0;width:872px;height:1038px;background:var(--white);
  border-radius:0 0 6px 6px;box-shadow:0 2px 6px rgba(0,0,0,.18)}
.brand{left:138px;top:60px;display:flex;align-items:center;gap:8px;white-space:nowrap}
.brand-dot{width:22px;height:22px;border-radius:50%;background:var(--blue-dark);flex:none}
.brand-name{font-family:Arial,Helvetica,sans-serif;font-size:17px;color:var(--ink)}
.social{left:535px;top:76px;display:flex;align-items:center;gap:10px;font-size:14px;color:var(--ink)}
.social span.dot{width:30px;height:30px;border-radius:50%;background:var(--blue)}
.call{left:790px;top:62px;text-align:right;width:165px;font-family:Raleway,sans-serif}
.call-label{font-size:18px;color:var(--ink);padding-right:32px}
.call-num{display:flex;align-items:center;justify-content:flex-end;gap:8px;font-size:20px;color:var(--blue);margin-top:5px}
.nav{left:102px;top:159px;width:864px;height:41px;display:flex;border-radius:3px;
  background:linear-gradient(180deg,var(--blue-light),var(--blue-dark))}
.nav a{display:flex;align-items:center;justify-content:center;color:var(--white);text-decoration:none;
  font-family:"Open Sans",sans-serif;font-size:13px;border-right:1px solid rgba(0,0,0,.25);box-shadow:1px 0 rgba(255,255,255,.15);position:relative}
.nav a:last-child{border:none;box-shadow:none}
.nav .active::after{content:"";position:absolute;bottom:5px;left:50%;margin-left:-4px;border:4px solid transparent;border-top-color:#fff}
.rule-black{left:102px;top:203px;width:864px;height:6px;background:var(--ink)}
.slider{left:105px;top:215px;width:856px;height:302px;border:1px solid #e3e3e3;
  background:linear-gradient(90deg,#fdfdfe 0%,#f1f3f6 50%,#e4e8ed 100%);overflow:hidden}
.slide-photo{left:430px;top:0;width:426px;height:302px;
  background:linear-gradient(160deg,#eef0f3 0%,#b9c0c8 30%,#e2e5e9 45%,#8f99a4 60%,#d6dade 75%,#f0f2f4 100%)}
.slide-title{left:46px;top:58px;font-family:"Libre Baskerville",serif;font-weight:700;font-size:22px;letter-spacing:1px;color:var(--blue)}
.slide-sub{left:73px;top:115px;font-family:Raleway,sans-serif;font-size:17px;color:var(--ink)}
.learn{left:123px;top:178px;width:224px;height:47px;border-radius:4px;
  background:linear-gradient(180deg,var(--blue-light),var(--blue-dark));display:flex;align-items:center;
  padding-left:16px;gap:14px;font-family:"Libre Baskerville",serif;font-weight:700;font-size:18px;color:#fff;letter-spacing:.5px}
.circle-arrow{display:block}
.arrow-btn{top:121px;width:36px;height:36px;background:var(--ink);display:flex;align-items:center;justify-content:center}
.dots{left:24px;top:286px;display:flex;gap:9px}
.dots i{width:12px;height:12px;border-radius:50%;background:var(--blue)}
.dots i.on{background:var(--ink)}
.dropdown{left:345px;top:207px;width:153px;height:81px;background:rgba(61,103,151,.85);padding:7px 5px}
.dropdown div{height:25px;border-radius:5px;font-family:"Open Sans",sans-serif;font-size:13px;color:#fff;padding:3px 0 0 30px;margin-bottom:7px}
.dropdown div.cur{background:#fff;color:var(--ink)}
.sec-title{font-family:Raleway,sans-serif;font-size:16px;color:var(--ink);font-weight:400}
.sec-title b{font-weight:400;color:var(--blue-dark)}
.welcome{left:120px;top:550px}
.hr{height:1px;background:var(--grey-line)}
.copy{left:121px;top:593px;width:572px;font-size:12px;line-height:17.5px;text-align:justify;color:var(--text)}
.copy p{margin-bottom:8px}
.small-btn{border-radius:4px;background:linear-gradient(180deg,var(--blue-light),var(--blue-dark));color:#fff;font-size:12px;
  display:flex;align-items:center;justify-content:center}
.cat{left:730px;top:539px;width:231px;height:224px;border:1px solid #e6e6e6;border-radius:6px;background:#fbfbfc;text-align:center}
.cat-sub{font-family:Raleway,sans-serif;font-size:13px;color:var(--blue-dark);margin-top:6px}
.cat-sub span{color:var(--ink)}
.cat-book{width:72px;height:80px;margin:10px auto 0;transform:skewY(-5deg);
  background:linear-gradient(135deg,#9db4cc,#d8c9a8 60%,#6b7f93);box-shadow:2px 3px 4px rgba(0,0,0,.3)}
.dl{width:146px;height:44px;margin:14px auto 0;background:var(--ink);border:3px solid #fff;box-shadow:0 0 4px rgba(0,0,0,.3);
  display:flex;align-items:center;gap:10px;padding-left:10px;font-family:Raleway,sans-serif;font-size:19px;color:#fff}
.cards{left:114px;top:827px;display:flex;gap:12px}
.card{width:158px}
.card-photo{height:154px;border:3px solid #eee}
.p-rail{background:linear-gradient(150deg,#f4f5f7 0%,#c7ccd2 45%,#8e96a0 70%,#e9ecef 100%)}
.p-glass{background:linear-gradient(135deg,#e6e8eb 0%,#a57a6c 40%,#6e4f48 55%,#c9ccd0 80%,#eef0f2 100%)}
.p-post{background:linear-gradient(180deg,#4a4d52 0%,#9aa0a7 40%,#dfe3e7 75%,#f2f3f5 100%)}
.p-tube{background:linear-gradient(180deg,#fafafa 0%,#e8e9ea 30%,#a9adb1 45%,#d2d4d6 60%,#fafafa 100%)}
.p-door{background:linear-gradient(160deg,#6d737a 0%,#c3c8cd 40%,#8d979d 60%,#a9c2c0 100%)}
.card-label{height:26px;margin-top:6px;background:var(--blue);display:flex;align-items:center;gap:8px;padding-left:5px;font-size:12px;color:#fff}
.footer{left:0;top:1084px;width:1066px;height:116px;background:var(--footer)}
.f-links{left:109px;top:37px;display:flex;font-family:"Open Sans",sans-serif;font-size:12px;color:#fff}
.f-links span{margin-right:22px}
.f-links em{font-style:normal;margin-right:22px}
.f-copy{left:108px;top:76px;font-size:12px;color:#fff}
.f-brand{left:826px;top:48px;display:flex;align-items:center;gap:7px;white-space:nowrap}
.f-brand .brand-dot{width:16px;height:16px;background:#999}
.f-brand .brand-name{color:#fff;font-size:13px}
</style>
</head>
<body>
<div class="page"></div>

<div class="abs brand">
  <span class="brand-dot"></span>
  <span class="brand-name">Harlow Birch Metal</span>
</div>

<div class="abs social">Stay connected <span class="dot"></span><span class="dot"></span></div>

<div class="abs call">
  <div class="call-label">Call Now</div>
  <div class="call-num">
    <svg width="26" height="26" viewBox="0 0 26 26"><circle cx="13" cy="13" r="12" fill="#e6e8eb"/><path d="M9 7c1-1 2 0 2.5 1.5s0 2-1 2.5c.8 2 2 3.3 4 4 .5-1 1-1.7 2.5-1s2.5 1.5 1.5 2.5c-2 2-5 .5-7.5-2S7 9 9 7z" fill="#555"/></svg>
    555-014-2286
  </div>
</div>

<nav class="abs nav">
  <a style="width:99px">HOME</a>
  <a style="width:136px">ABOUT US</a>
  <a class="active" style="width:162px">PRODUCTS</a>
  <a style="width:160px">DOWNLOAD</a>
  <a style="width:183px">ONLINE ENQUIRY</a>
  <a style="width:124px">CONTACT US</a>
</nav>
<div class="abs rule-black"></div>

<section class="abs slider">
  <div class="abs slide-photo" role="img" aria-label="Photo of a brushed stainless steel handrail with glass clamp post"></div>
  <div class="abs slide-title">PROFESSIONAL SUPPLIER FOR</div>
  <div class="abs slide-sub">STAINLESS STEEL RAILING &amp; GLASS SYSTEM</div>
  <div class="abs learn">LEARN MORE
    <svg class="circle-arrow" width="34" height="34" viewBox="0 0 34 34"><circle cx="17" cy="17" r="16" fill="#e8e8e8"/><path d="M14 10l7 7-7 7" stroke="#333" stroke-width="3" fill="none"/></svg>
  </div>
  <div class="abs arrow-btn" style="left:1px"><svg width="14" height="20"><path d="M11 2L3 10l8 8" stroke="#fff" stroke-width="3" fill="none"/></svg></div>
  <div class="abs arrow-btn" style="left:818px"><svg width="14" height="20"><path d="M3 2l8 8-8 8" stroke="#fff" stroke-width="3" fill="none"/></svg></div>
  <div class="abs dots"><i></i><i class="on"></i><i></i><i></i></div>
</section>

<div class="abs dropdown">
  <div class="cur">Product 1</div>
  <div>Product 2</div>
</div>

<div class="abs welcome">
  <h2 class="sec-title"><b>WELCOME TO</b> HARLOW BIRCH METAL</h2>
  <div class="hr" style="width:572px;margin-top:10px"></div>
</div>
<div class="abs copy">
  <p>Lorem Ipsum is simply dummy text of the printing and typesetting industry. Lorem Ipsum has been the industry's standard dummy text ever since the 1500s, when an unknown printer took a galley of type and scrambled it to .</p>
  <p>It has survived not only five centuries, but also the leap into electronic typesetting, remaining essentially unchanged. It was popularised in the 1960s with the release of Tresslet sheets containing Lorem Ipsum passages, and more recently with desktop publishing software like Ardel PageForge including It has survived not only five centuries, but also the leap into electronic typesetting, remaining essentially</p>
</div>
<div class="abs small-btn" style="left:617px;top:734px;width:74px;height:26px">Read More</div>

<aside class="abs cat">
  <div class="sec-title" style="margin-top:15px;font-size:16px"><b>DOWNLOAD</b> CATALOGUE</div>
  <div class="cat-sub">OUR <span>2013</span> CATALOGUE</div>
  <div class="cat-book" role="img" aria-label="Cover of the product catalogue"></div>
  <div class="dl">
    <svg width="18" height="34" viewBox="0 0 18 34"><rect x="5" y="0" width="8" height="20" fill="#3a8ad8"/><path d="M0 18h18L9 32z" fill="#3a8ad8"/></svg>
    Download
  </div>
</aside>

<div class="abs" style="left:114px;top:780px">
  <h2 class="sec-title"><b>OUR</b> PRODUCTS</h2>
  <div class="hr" style="width:843px;margin-top:10px"></div>
</div>

<div class="abs cards">
  <div class="card"><div class="card-photo p-rail" role="img" aria-label="Photo of stainless railing bracket"></div>
    <div class="card-label"><svg width="20" height="20"><circle cx="10" cy="10" r="9" fill="#ddd"/><path d="M8 5l5 5-5 5" stroke="#333" stroke-width="2" fill="none"/></svg>Railing Systems</div></div>
  <div class="card"><div class="card-photo p-glass" role="img" aria-label="Photo of glass standoff fitting"></div>
    <div class="card-label"><svg width="20" height="20"><circle cx="10" cy="10" r="9" fill="#ddd"/><path d="M8 5l5 5-5 5" stroke="#333" stroke-width="2" fill="none"/></svg>Glass system</div></div>
  <div class="card"><div class="card-photo p-post" role="img" aria-label="Photo of post and glass balustrade"></div>
    <div class="card-label"><svg width="20" height="20"><circle cx="10" cy="10" r="9" fill="#ddd"/><path d="M8 5l5 5-5 5" stroke="#333" stroke-width="2" fill="none"/></svg>Post &amp; Balustrade</div></div>
  <div class="card"><div class="card-photo p-tube" role="img" aria-label="Photo of square tube T fitting"></div>
    <div class="card-label"><svg width="20" height="20"><circle cx="10" cy="10" r="9" fill="#ddd"/><path d="M8 5l5 5-5 5" stroke="#333" stroke-width="2" fill="none"/></svg>Square tube Fittings</div></div>
  <div class="card"><div class="card-photo p-door" role="img" aria-label="Photo of sliding door roller hardware"></div>
    <div class="card-label"><svg width="20" height="20"><circle cx="10" cy="10" r="9" fill="#ddd"/><path d="M8 5l5 5-5 5" stroke="#333" stroke-width="2" fill="none"/></svg>Sliding door &amp; Conopy</div></div>
</div>

<footer class="abs footer">
  <div class="abs f-links">
    <span>Home</span><em>/</em><span>About Us</span><em>/</em><span>Products</span><em>/</em><span>Download</span><em>/</em><span>online enquiry</span><em>/</em><span>Contact Us</span>
  </div>
  <div class="abs f-copy">2013 Harlow Birch Metal. All Rights Reserved.</div>
  <div class="abs f-brand">
    <span class="brand-dot"></span>
    <span class="brand-name">Harlow Birch Metal</span>
  </div>
</footer>
</body>
</html>
```